Landing Page Design for Adult Dating Age Verification (18+)

The objective of this task is to design a visually appealing pre-landing page for the adult dating site "Pivolunda (site: https://pivolunda.example/)" with an age verification mechanism. The pre-landing page will feature two buttons that redirect visitors to the main offer. The design should also include a footer block that includes links to the terms of use, privacy policy, and contact us pages.

Design Requirements:
Develop an age verification section prominently displayed on the pre-landing page.
Design the section to include two buttons labeled "Yes" and "No" for visitors to confirm their age.
Ensure the section is visually appealing and clearly communicates the purpose of age verification.

Visual Appeal:
Create a visually appealing design that aligns with the branding and theme of the "Pivolunda" adult dating site.
Use suitable color schemes, typography, and graphics to enhance the overall visual appeal of the pre-landing page.

Layout and Navigation:
Design an engaging and intuitive layout that encourages visitors to interact with the page and proceed to the main offer.
Ensure clear and visible navigation elements that direct visitors to the main offer or provide additional information.

Responsive Design:
Develop a responsive design that provides a seamless user experience across various devices, including desktop and mobile.
Ensure the design elements and layout adapt well to different screen sizes and resolutions.

File Formats and Assets:
Deliver the final design in PSD, AI, or Sketch format, ensuring that the files are well-organized and layered.
Include any necessary images or assets used in the design, ensuring they are of high quality and optimized for web use.

```html
<!DOCTYPE html>
<html lang="en">
<head>
<meta charset="utf-8">
<title>Pivolunda – Age Verification</title>
<link href="https://fonts.googleapis.com/css2?family=Quicksand:wght@500;600;700&display=swap" rel="stylesheet">
<style>
  :root {
    --scene-dark: #2b2a2e;
    --scene-mid: #5a5258;
    --scene-warm: #6b3a44;
    --scene-light: #8d8a8c;
    --panel: rgba(30, 29, 32, 0.86);
    --lilac: #d6b6dc;
    --white: #ffffff;
    --muted: rgba(255, 255, 255, 0.72);
    --crimson: #c80f50;
    --navy: #1a2736;
  }
  * { box-sizing: border-box; margin: 0; padding: 0; }
  html, body { width: 1200px; height: 547px; overflow: hidden; }
  body {
    position: relative;
    font-family: "Quicksand", sans-serif;
    background: var(--scene-dark);
  }
  .hero-backdrop {
    position: absolute;
    inset: 0;
    background:
      radial-gradient(ellipse 220px 300px at 150px 330px, var(--scene-light) 0%, transparent 70%),
      radial-gradient(ellipse 260px 280px at 1000px 300px, var(--scene-light) 0%, transparent 70%),
      radial-gradient(ellipse 180px 140px at 420px 470px, var(--scene-warm) 0%, transparent 75%),
      radial-gradient(ellipse 200px 120px at 1130px 340px, var(--scene-warm) 0%, transparent 75%),
      linear-gradient(90deg, var(--scene-mid) 0%, var(--scene-dark) 45%, var(--scene-mid) 75%, var(--scene-dark) 100%);
  }
  .hero-backdrop::after {
    content: "";
    position: absolute;
    inset: 0;
    background: rgba(20, 20, 24, 0.35);
  }
  .music-toggle {
    position: absolute;
    left: 1061px;
    top: 19px;
    width: 40px;
    height: 40px;
    background: var(--navy);
    border: 2px solid var(--crimson);
    display: flex;
    align-items: center;
    justify-content: center;
  }
  .age-gate {
    position: absolute;
    left: 334px;
    top: 95px;
    width: 532px;
    height: 357px;
    border-radius: 10px;
    background: var(--panel);
    text-align: center;
  }
  .brand {
    position: absolute;
    top: 56px;
    left: 0;
    right: 0;
    display: flex;
    align-items: center;
    justify-content: center;
    gap: 10px;
  }
  .brand-dot {
    width: 46px;
    height: 46px;
    border-radius: 50%;
    background: var(--lilac);
  }
  .brand-name {
    font-size: 36px;
    font-weight: 700;
    color: var(--lilac);
    letter-spacing: 0.5px;
    line-height: 1;
  }
  .gate-title {
    position: absolute;
    top: 145px;
    left: 0;
    right: 0;
    font-size: 39px;
    font-weight: 600;
    color: var(--lilac);
    line-height: 1;
  }
  .gate-question {
    position: absolute;
    top: 196px;
    left: 0;
    right: 0;
    font-size: 19px;
    font-weight: 600;
    color: var(--white);
    line-height: 24px;
  }
  .gate-actions {
    position: absolute;
    top: 235px;
    left: 0;
    right: 0;
    display: flex;
    justify-content: center;
    gap: 10px;
  }
  .gate-button {
    width: 54px;
    height: 41px;
    background: var(--crimson);
    color: var(--white);
    font-family: "Quicksand", sans-serif;
    font-size: 17px;
    font-weight: 700;
    border: none;
  }
  .remember {
    position: absolute;
    top: 289px;
    left: 207px;
    display: flex;
    align-items: center;
    gap: 11px;
    font-size: 13px;
    font-weight: 600;
    color: var(--white);
    line-height: 16px;
  }
  .remember-box {
    width: 9px;
    height: 9px;
    background: var(--white);
  }
  .site-footer {
    position: absolute;
    left: 0;
    right: 0;
    bottom: 10px;
    display: flex;
    justify-content: center;
    gap: 22px;
    font-size: 12px;
    font-weight: 600;
    line-height: 16px;
  }
  .footer-link {
    color: var(--muted);
    text-decoration: none;
  }
</style>
</head>
<body>
  <div class="hero-backdrop" role="img" aria-label="Blurred photo of young women chatting and laughing on a sofa"></div>

  <div class="music-toggle" aria-label="Toggle music">
    <svg width="22" height="22" viewBox="0 0 24 24" fill="none" stroke="#ffffff" stroke-width="2">
      <path d="M9 18V5l11-2v13"/>
      <circle cx="6" cy="18" r="3" fill="#ffffff"/>
      <circle cx="17" cy="16" r="3" fill="#ffffff"/>
    </svg>
  </div>

  <section class="age-gate">
    <div class="brand">
      <span class="brand-dot"></span>
      <span class="brand-name">Pivolunda</span>
    </div>
    <h1 class="gate-title">Find Your Match</h1>
    <p class="gate-question">Are You Over 18 years of Age?</p>
    <div class="gate-actions">
      <button class="gate-button">Yes</button>
      <button class="gate-button">No</button>
    </div>
    <label class="remember"><span class="remember-box"></span>Remember Me</label>
  </section>

  <footer class="site-footer">
    <a class="footer-link" href="https://pivolunda.example/terms">Terms of Use</a>
    <a class="footer-link" href="https://pivolunda.example/privacy">Privacy Policy</a>
    <a class="footer-link" href="https://pivolunda.example/contact">Contact Us</a>
  </footer>
</body>
</html>
```